Morvela Aesthetic Doctor

I require an elegant, luxurious looking business card for my aesthetic business. I am a doctor and that will set me aside from competitors. I am planning to provide home and spa based treatments to clients with high expectations. I have attached my logo.

```html
<!DOCTYPE html>
<html lang="en">
<head>
<meta charset="utf-8">
<title>Morvela Aesthetic Doctor – Business Card</title>
<link href="https://fonts.googleapis.com/css2?family=Arimo:wght@400;700&family=Patrick+Hand&display=swap" rel="stylesheet">
<style>
  :root {
    --page-bg: #ffffff;
    --card-blue: #0f6fc4;
    --crescent-grey: #a7a9ac;
    --card-white: #ffffff;
    --brand-grey: #8d9095;
    --text-blue: #1f64b4;
    --social-navy: #0d5aa0;
    --icon-sky: #4db0ea;
    --text-light: #ffffff;
  }
  * { margin: 0; padding: 0; box-sizing: border-box; }
  html, body {
    width: 1200px;
    height: 806px;
    overflow: hidden;
    background: var(--page-bg);
    font-family: "Arimo", Arial, sans-serif;
  }
  .card {
    position: absolute;
    left: 132px;
    top: 104px;
    width: 936px;
    height: 594px;
    overflow: hidden;
    box-shadow: 0 2px 14px rgba(0, 0, 0, 0.14);
  }
  .card-shapes {
    position: absolute;
    inset: 0;
    display: block;
  }
  .brand-side {
    position: absolute;
    left: 0;
    top: 0;
    width: 544px;
    height: 100%;
    text-align: center;
  }
  .brand-mark {
    position: absolute;
    left: 230px;
    top: 148px;
    width: 84px;
    height: 84px;
    border: 3px solid var(--brand-grey);
    border-radius: 50%;
  }
  .brand-name {
    position: absolute;
    left: 0;
    width: 100%;
    top: 262px;
    color: var(--brand-grey);
    font-weight: 400;
    font-size: 46px;
    letter-spacing: 3px;
    line-height: 1;
  }
  .brand-tagline {
    position: absolute;
    left: 0;
    width: 100%;
    top: 316px;
    color: var(--brand-grey);
    font-weight: 400;
    font-size: 22px;
    letter-spacing: 2px;
    line-height: 1;
  }
  .service-mode {
    position: absolute;
    left: 0;
    width: 100%;
    top: 356px;
    font-family: "Patrick Hand", cursive;
    font-size: 21px;
    color: var(--text-blue);
    letter-spacing: 0.5px;
  }
  .service-list {
    position: absolute;
    left: 0;
    width: 100%;
    top: 400px;
    font-size: 15px;
    line-height: 20px;
    color: var(--text-blue);
  }
  .service-list .sep { margin: 0 12px; }
  .social-links {
    position: absolute;
    left: 0;
    width: 100%;
    top: 453px;
    display: flex;
    justify-content: center;
    gap: 12px;
  }
  .social-links span {
    width: 31px;
    height: 31px;
    border-radius: 50%;
    background: var(--social-navy);
  }
  .doctor {
    position: absolute;
    right: 108px;
    top: 137px;
    text-align: right;
    color: var(--text-light);
  }
  .doctor-name {
    font-size: 19px;
    font-weight: 700;
    white-space: pre;
  }
  .doctor-credential {
    margin-top: 8px;
    font-size: 15.5px;
  }
  .contacts {
    position: absolute;
    right: 112px;
    top: 340px;
    list-style: none;
    color: var(--text-light);
    font-size: 17px;
  }
  .contacts li {
    display: flex;
    align-items: center;
    justify-content: flex-end;
    height: 40px;
    margin-bottom: 9px;
  }
  .contacts .icon {
    width: 39px;
    height: 39px;
    margin-left: 18px;
    border-radius: 50%;
    background: var(--icon-sky);
    display: flex;
    align-items: center;
    justify-content: center;
  }
  .contacts svg { width: 20px; height: 20px; }
</style>
</head>
<body>
  <main class="card">
    <svg class="card-shapes" viewBox="0 0 936 594" width="936" height="594" aria-hidden="true">
      <rect width="936" height="594" fill="var(--card-blue)"/>
      <circle cx="214.3" cy="291.8" r="323.5" fill="var(--crescent-grey)"/>
      <circle cx="124.8" cy="291.6" r="370.8" fill="var(--card-white)"/>
    </svg>

    <section class="brand-side">
      <div class="brand-mark"></div>
      <div class="brand-name">MORVELA</div>
      <div class="brand-tagline">AESTHETIC DOCTOR</div>
      <p class="service-mode">Home and Spa Based Treatments</p>
      <p class="service-list">
        Dermal injectables<span class="sep">.</span>Plasma facials<span class="sep">.</span>Microneedling<br>
        Skin boosters<span class="sep">.</span>Excessive sweating
      </p>
      <div class="social-links">
        <span aria-label="Social profile"></span>
        <span aria-label="Social profile"></span>
      </div>
    </section>

    <section class="doctor">
      <h1 class="doctor-name">Dr. Elin Varro  MRCPCH MD</h1>
      <p class="doctor-credential">Australasian Diploma of Asthetic Medicine</p>
    </section>

    <ul class="contacts">
      <li>0800 555 014
        <span class="icon">
          <svg viewBox="0 0 20 20" fill="none" stroke="#fff" stroke-width="1.4" stroke-linejoin="round">
            <path d="M3 8c0-2 3-3.5 7-3.5S17 6 17 8l-3 .6-.6-1.6H6.6L6 8.6z"/>
            <path d="M6 9.5h8l1.5 5.5h-11z"/>
            <circle cx="10" cy="12.2" r="1.3"/>
          </svg>
        </span>
      </li>
      <li>elin@morvela.co.nz
        <span class="icon">
          <svg viewBox="0 0 20 20" fill="none" stroke="#fff" stroke-width="1.4" stroke-linejoin="round">
            <rect x="3.5" y="5.5" width="13" height="9" rx="1"/>
            <path d="M3.5 6l6.5 5 6.5-5"/>
          </svg>
        </span>
      </li>
      <li>www.morvela.co.nz
        <span class="icon">
          <svg viewBox="0 0 20 20" fill="none" stroke="#fff" stroke-width="1.4">
            <circle cx="10" cy="10" r="6.5"/>
            <ellipse cx="10" cy="10" rx="2.8" ry="6.5"/>
            <path d="M3.5 10h13"/>
          </svg>
        </span>
      </li>
    </ul>
  </main>
</body>
</html>
```